Brevora Ad Image Design Competition

We're seeking creative designers to develop a series of engaging Brevora advertisements for Moltcraft with original art work.

The goal is to create scroll-stopping ads that capture attention through humor, nostalgia, and compelling storytelling while maintaining professional appeal.

Creative Brief:
Please read the "Core Messages to Convey"
https://pages.quillbarn.net/sheet/p/7kRtw2QmLv9xNcBe4HjYa63-s08ZueTFd_q51hnWpZ3/view?tab=t.0#heading=h.4mrwtzcja2k

Target Market(s)

Busy executives focusing on making their company more efficient

Requirements
Must have
• An image ( not copy) that speaks to one of our "Core Messages to Convey"

```html
<!DOCTYPE html>
<html lang="en">
<head>
<meta charset="utf-8">
<title>Moltcraft – Accelerate Your Value Creation Journey</title>
<link rel="stylesheet" href="https://fonts.googleapis.com/css2?family=Bebas+Neue&family=Montserrat:wght@500;600;800&display=swap">
<style>
  :root {
    --ink: #15131c;
    --brand-red: #d3272a;
    --paper: #ffffff;
    --runner-top: #c23a8a;
    --runner-bottom: #2a2f7a;
    --goal-red: #d3272a;
    --goal-gold: #f2b233;
  }
  * { margin: 0; padding: 0; box-sizing: border-box; }
  html, body {
    width: 1200px;
    height: 1200px;
    overflow: hidden;
    background: var(--paper);
  }
  .ad {
    position: relative;
    width: 1200px;
    height: 1200px;
    background: var(--paper);
    overflow: hidden;
  }
  .headline {
    position: absolute;
    left: 0;
    top: 0;
    width: 1200px;
    height: 680px;
  }
  .headline__accelerate,
  .headline__value {
    font-family: "Bebas Neue", "Arial Narrow", sans-serif;
    font-size: 318px;
  }
  .headline__accelerate { fill: var(--ink); }
  .headline__value { fill: var(--brand-red); }
  .headline__journey {
    font-family: "Montserrat", Arial, sans-serif;
    font-weight: 800;
    font-size: 94px;
    fill: var(--ink);
  }

  .growth-steps {
    position: absolute;
    left: 0;
    top: 0;
    width: 1200px;
    height: 1200px;
  }
  .growth-steps__red { fill: var(--brand-red); }
  .growth-steps__dark { fill: var(--ink); }

  .runner-illustration {
    position: absolute;
    left: 289px;
    top: 846px;
    width: 240px;
    height: 275px;
    border-radius: 40px;
    background: linear-gradient(180deg, var(--runner-top) 0%, var(--runner-bottom) 100%);
    opacity: 0.85;
  }
  .goal-illustration {
    position: absolute;
    left: 578px;
    top: 690px;
    width: 298px;
    height: 173px;
    border-radius: 90px 90px 0 0;
    background: linear-gradient(90deg, var(--goal-red) 0%, var(--goal-red) 62%, var(--goal-gold) 100%);
  }

  .brand-name,
  .brand-url {
    position: absolute;
    writing-mode: vertical-rl;
    transform: rotate(180deg);
    white-space: nowrap;
    font-family: "Montserrat", Arial, sans-serif;
    line-height: 1;
  }
  .brand-name {
    left: 60px;
    top: 818px;
    height: 336px;
    display: flex;
    align-items: center;
    justify-content: flex-start;
    gap: 16px;
    font-size: 54px;
    font-weight: 600;
    color: var(--ink);
  }
  .brand-name__dot {
    width: 28px;
    height: 28px;
    border-radius: 50%;
    background: var(--ink);
  }
  .brand-url {
    left: 1122px;
    top: 848px;
    height: 306px;
    font-size: 30px;
    font-weight: 500;
    color: var(--brand-red);
  }
</style>
</head>
<body>
  <main class="ad">
    <svg class="headline" viewBox="0 0 1200 680" aria-label="Accelerate your value creation journey">
      <text class="headline__accelerate" x="84" y="324" textLength="1034" lengthAdjust="spacingAndGlyphs">ACCELERATE</text>
      <text class="headline__value" x="77" y="568" textLength="1051" lengthAdjust="spacingAndGlyphs">YOUR VALUE</text>
      <text class="headline__journey" x="86" y="658" textLength="1028" lengthAdjust="spacingAndGlyphs">CREATION&#160;&#160;JOURNEY</text>
    </svg>

    <svg class="growth-steps" viewBox="0 0 1200 1200" aria-label="Rising bar steps">
      <rect class="growth-steps__dark" x="626" y="863" width="254" height="360" rx="8"/>
      <rect class="growth-steps__red" x="514" y="935" width="222" height="290" rx="8"/>
      <rect class="growth-steps__dark" x="390" y="1047" width="191" height="180" rx="8"/>
      <rect class="growth-steps__red" x="280" y="1116" width="191" height="110" rx="8"/>
    </svg>

    <div class="goal-illustration" role="img" aria-label="Illustration of a red target hit by an arrow beside a gold trophy on the top step"></div>
    <div class="runner-illustration" role="img" aria-label="Illustration of a person running up the steps"></div>

    <div class="brand-name">
      <span class="brand-name__dot"></span>
      <span class="brand-name__text">Moltcraft</span>
    </div>

    <div class="brand-url">www.moltcraft.co</div>
  </main>
</body>
</html>
```